Vorapo Business Card

Need a double sided business card. Would like the business card to have the logo on one side and the employees details and business contact details on the other.

Business

```html
<!DOCTYPE html>
<html lang="en">
<head>
<meta charset="utf-8">
<title>Vorapo Business Card</title>
<link rel="stylesheet" href="https://fonts.googleapis.com/css2?family=Open+Sans:wght@400;700&family=PT+Serif:wght@400;700&display=swap">
<style>
  :root {
    --backdrop: #262626;
    --card-white: #fdfdfd;
    --brand-green: #9cc83c;
    --brand-grey: #77797d;
    --text-white: #ffffff;
  }
  * { box-sizing: border-box; margin: 0; padding: 0; }
  html, body { width: 1200px; height: 734px; overflow: hidden; }
  body {
    background: var(--backdrop);
    font-family: "Open Sans", Arial, sans-serif;
    position: relative;
  }
  .card {
    position: absolute;
    top: 217px;
    width: 520px;
    height: 300px;
    border-radius: 22px;
    overflow: hidden;
    box-shadow: 0 12px 30px rgba(0,0,0,0.45);
  }
  .card--details { left: 50px; background: var(--card-white); }
  .card--logo { left: 630px; background: var(--brand-green); }

  .details__band {
    position: absolute; left: 0; right: 0; top: 170px; bottom: 0;
    background: var(--brand-green);
    border-top: 8px solid var(--brand-grey);
  }
  .wordmark {
    font-family: "Open Sans", Arial, sans-serif;
    font-weight: 700;
    letter-spacing: 1px;
    display: flex; align-items: center;
  }
  .wordmark__dot { display: inline-block; background: currentColor; }
  .details__wordmark {
    position: absolute; right: 34px; top: 82px;
    color: var(--brand-green); font-size: 46px; gap: 10px;
  }
  .details__wordmark .wordmark__dot { width: 14px; height: 14px; }

  .contact-list {
    position: absolute; right: 30px; top: 22px;
    list-style: none; color: var(--text-white);
    font-size: 11px; line-height: 17px; text-align: right;
  }
  .contact-list li { display: flex; justify-content: flex-end; align-items: center; gap: 7px; }
  .contact-list svg { width: 10px; height: 10px; fill: none; stroke: var(--text-white); stroke-width: 1.4; }

  .person {
    position: absolute; left: 32px; bottom: 26px; color: var(--text-white);
    font-family: "PT Serif", Georgia, serif;
  }
  .person__name { font-size: 20px; font-weight: 700; }
  .person__role { font-size: 12px; }

  .logo__wordmark {
    position: absolute; inset: 0; justify-content: center;
    color: var(--brand-grey); font-size: 64px; gap: 14px;
  }
  .logo__wordmark .wordmark__dot { width: 18px; height: 18px; }
</style>
</head>
<body>
  <section class="card card--details">
    <div class="wordmark details__wordmark">vorapo<span class="wordmark__dot"></span></div>
    <div class="details__band">
      <ul class="contact-list">
        <li>00 - 0000 - 0000
          <svg viewBox="0 0 10 10"><path d="M2 1 L4 1 L4.5 3 L3.5 4 Q5 6.5 6 6.5 L7 5.5 L9 6 L9 8 Q5 9 1.5 4 Q1 2 2 1Z"/></svg></li>
        <li>00 - 0000 - 0000
          <svg viewBox="0 0 10 10"><rect x="2.5" y="0.8" width="5" height="8.4" rx="1"/></svg></li>
        <li>info@vorapo.com
          <svg viewBox="0 0 10 10"><rect x="0.8" y="2" width="8.4" height="6"/><path d="M0.8 2 L5 5.5 L9.2 2"/></svg></li>
        <li>www.vorapo.com
          <svg viewBox="0 0 10 10"><circle cx="5" cy="5" r="4"/><path d="M1 5 H9 M5 1 Q2.5 5 5 9 Q7.5 5 5 1"/></svg></li>
      </ul>
      <div class="person">
        <p class="person__name">Marek Dalton</p>
        <p class="person__role">Director</p>
      </div>
    </div>
  </section>

  <section class="card card--logo">
    <div class="wordmark logo__wordmark">vorapo<span class="wordmark__dot"></span></div>
  </section>
</body>
</html>
```